Attorney Business Card

I need a business card that looks professional yet modern. I am an Attorney. , I need a professional yet modern business card for my law practice. My logo and information have been uploaded. , I need a business card that looks professional yet modern. I am an Attorney. , I need a professional yet modern business card for my law practice. My logo and information have been uploaded.

Industry/Entity Type

Business

Requirements
Must have
• My logo which has been uploaded , my logo , My logo which has been uploaded , my logo

```html
<!DOCTYPE html>
<html lang="en">
<head>
<meta charset="utf-8">
<title>Orvane Law Firm – Business Card</title>
<link rel="stylesheet" href="https://fonts.googleapis.com/css2?family=Open+Sans:wght@300;400;700&display=swap">
<style>
  :root {
    --stage: #3a3a3a;
    --card: #ebebeb;
    --accent: #16aeea;
    --ink: #3b3b3b;
    --ink-soft: #6b6b6b;
  }
  * { margin: 0; padding: 0; box-sizing: border-box; }
  html, body { width: 1200px; height: 705px; overflow: hidden; }
  body {
    background: var(--stage);
    font-family: "Open Sans", Arial, sans-serif;
    position: relative;
  }
  .card {
    position: absolute;
    left: 100px; top: 68px;
    width: 1000px; height: 570px;
    background: var(--card);
  }
  .accent-band {
    position: absolute;
    left: 620px; top: 0;
    width: 30px; height: 100%;
    background: var(--accent);
  }
  .brand {
    position: absolute;
    left: 0; width: 620px;
    top: 150px;
    display: flex; align-items: center; justify-content: center; gap: 14px;
  }
  .brand-dot {
    width: 26px; height: 26px; border-radius: 50%;
    background: var(--accent);
  }
  .brand-name {
    color: var(--accent);
    font-weight: 400;
    font-size: 36px;
    letter-spacing: 2px;
    text-transform: uppercase;
  }
  .identity {
    position: absolute;
    left: 0; width: 620px;
    top: 300px;
    text-align: center;
  }
  .person-name {
    color: var(--ink);
    font-weight: 700;
    font-size: 34px;
    letter-spacing: 0.5px;
  }
  .person-title {
    margin-top: 6px;
    color: var(--ink);
    font-weight: 300;
    font-size: 22px;
    letter-spacing: 10px;
    text-transform: uppercase;
  }
  .icon-strip {
    position: absolute;
    left: 720px; top: 255px;
    width: 34px; height: 315px;
    background: var(--accent);
  }
  .contact-list {
    position: absolute;
    left: 720px; top: 255px;
    list-style: none;
  }
  .contact-item {
    display: flex; align-items: flex-start;
    margin-bottom: 22px;
  }
  .contact-icon {
    width: 34px; height: 24px;
    display: flex; align-items: center; justify-content: center;
    flex-shrink: 0;
  }
  .contact-icon svg { width: 20px; height: 20px; }
  .contact-text {
    margin-left: 16px;
    color: var(--ink-soft);
    font-size: 13px;
    letter-spacing: 1.5px;
    line-height: 18px;
    text-transform: uppercase;
    padding-top: 3px;
  }
  .contact-text.lower { text-transform: uppercase; }
</style>
</head>
<body>
  <div class="card">
    <div class="accent-band"></div>

    <div class="brand">
      <span class="brand-dot"></span>
      <span class="brand-name">Orvane Law Firm</span>
    </div>

    <div class="identity">
      <p class="person-name">DANIEL ORVANE, ESQ.</p>
      <p class="person-title">Attorney at Law</p>
    </div>

    <div class="icon-strip"></div>
    <ul class="contact-list">
      <li class="contact-item">
        <span class="contact-icon">
          <svg viewBox="0 0 20 20"><path d="M10 2 L19 10 H16 V18 H12 V13 H8 V18 H4 V10 H1 Z" fill="#2e2e2e"/></svg>
        </span>
        <span class="contact-text">4820 Harbor Crest Blvd<br>Suite 1200<br>Lakeview Heights, CA 90000</span>
      </li>
      <li class="contact-item">
        <span class="contact-icon">
          <svg viewBox="0 0 20 20"><rect x="5" y="1" width="10" height="18" rx="2" fill="none" stroke="#2e2e2e" stroke-width="2"/><circle cx="10" cy="15.5" r="1.2" fill="#2e2e2e"/></svg>
        </span>
        <span class="contact-text">310.555.0142</span>
      </li>
      <li class="contact-item">
        <span class="contact-icon">
          <svg viewBox="0 0 20 20"><path d="M4 2 C2 4 2 7 5 11 C8 15 12 18 15 18 L18 15 L14 12 L12 14 C10 13 7 10 6 8 L8 6 L5 2 Z" fill="#2e2e2e"/></svg>
        </span>
        <span class="contact-text">310.555.0187</span>
      </li>
      <li class="contact-item">
        <span class="contact-icon">
          <svg viewBox="0 0 20 20"><rect x="5" y="2" width="10" height="5" fill="none" stroke="#2e2e2e" stroke-width="1.8"/><rect x="2" y="7" width="16" height="7" rx="1" fill="#2e2e2e"/><rect x="5" y="12" width="10" height="6" fill="#fff" stroke="#2e2e2e" stroke-width="1.5"/></svg>
        </span>
        <span class="contact-text">310.555.0199</span>
      </li>
      <li class="contact-item">
        <span class="contact-icon">
          <svg viewBox="0 0 20 20"><rect x="2" y="4" width="16" height="12" rx="1" fill="none" stroke="#2e2e2e" stroke-width="2"/><path d="M2 5 L10 11 L18 5" fill="none" stroke="#2e2e2e" stroke-width="2"/></svg>
        </span>
        <span class="contact-text">daniel@orvanelaw.com</span>
      </li>
      <li class="contact-item">
        <span class="contact-icon">
          <svg viewBox="0 0 20 20"><circle cx="10" cy="10" r="8" fill="none" stroke="#2e2e2e" stroke-width="1.8"/><ellipse cx="10" cy="10" rx="3.5" ry="8" fill="none" stroke="#2e2e2e" stroke-width="1.5"/><path d="M2 10 H18" stroke="#2e2e2e" stroke-width="1.5"/></svg>
        </span>
        <span class="contact-text">www.orvanelaw.com</span>
      </li>
    </ul>
  </div>
</body>
</html>
```